NOTE: I PROVIDED THE INCORRECT LOGO AND ONLY A HANDFUL OF PEOPLE NOTICED THAT IT WAS NOT THE ONE I DESCRIBED. THE LOGO I HAVE NOW ATTACHED MATCHES MY WEBSITE AND THE COLORS ON THE WEBSITE SHOULD BE USED FOR THE CARD.

PLEASE READ THE BUSINESS CARD DETAILS AND PROJECT MUST HAVES CAREFULLY.

I am looking for a business card that is powerful, a bit edgy, and although I work in the corporate world, not too formal. I would like to see designs that use the colors on my website www.brightmoorlane.com. I don't want the card to look washed out so please use shades of those colors that make them "pop". The "vibe" of the card needs to show substance and confidence while also reflecting that we're not your usual consultants.

The focus of my work is turning "people problems" into profits. Those problems could be poor service, an unstable workforce, untrained leaders, or managing change. We are an aggressive, results-focused team of performance improvement professionals who refuse to believe "things can't be done". For us, failure is not an option. Our logo reflects a target from the view of the site on a gun.

In addition to the contact information provided on the sample business card (do not include "turning people problems into profits"), I would like to include this statement (probably on the back):
I equip results-oriented business leaders to turn their people problems into profits in six months or less.

PLEASE NOTE THAT MY WEBSITE IS UNDER REVISION TO TONE DOWN THE MILITARY THEME, ALTHOUGH THE WARRIOR ENERGY AND FOCUS ON RESULTS REMAINS.

Target Market(s)

My clients are Mid and senior-level managers. I don't target any particular industry.

Industry/Entity Type

Consulting

Contact Information for Business Card

In addition to the contact information provided on the sample business card (DO NOT INCLUDE "turning people problems into profits"), I would like to include this statement (probably on the back):

I don't care whether the card is landscape or portrait view.

Font styles to use
Sans Serif

Requirements
Must have
• 1. be easy to read, no 6-8 point fonts!
• 2. a "vibe" that captures the eye without being too chaotic or busy
• 3. bold color, not washed out or boring - a good blend with the colors currently on my website (black, red, white, army green) but you don't need to use all of them.
• 4. all the contact information I have provided
• 5. a good blend with the colors currently on my website
• 6. Must have this quote on the back of the card: I equip results-oriented business leaders to turn their people problems into profits in six months or less.
Nice to have
• In looking at the sample images I provided for ideas, you can see that I like the way a card carries over from one side to the next.
• It would be great to find some aspect/quality/feature that I haven't seen before
Should not have
• 1. NO use of ALL CAPS
• 2. fonts that I would have to seek out and purchase (you should provide files for font if using something not standard)

```html
<!DOCTYPE html>
<html lang="en">
<head>
<meta charset="utf-8">
<title>Brightmoor Lane – Business Card</title>
<link href="https://fonts.googleapis.com/css2?family=Fira+Sans:wght@400;600&family=Questrial&display=swap" rel="stylesheet">
<style>
  :root {
    --backdrop: #0d0d0d;
    --card: #ffffff;
    --olive: #414531;
    --ink: #3a3a32;
    --muted: #55554d;
    --rule: #e6e6e2;
  }
  html, body {
    margin: 0;
    padding: 0;
    width: 1200px;
    height: 1200px;
    overflow: hidden;
    background: var(--backdrop);
  }
  .stage {
    position: relative;
    width: 1200px;
    height: 1200px;
  }
  .card {
    position: absolute;
    top: 446px;
    width: 548px;
    height: 310px;
    background: var(--card);
    overflow: hidden;
  }
  .card--front { left: 35px; }
  .card--back { left: 619px; }

  .emblem-circle {
    position: absolute;
    width: 304px;
    height: 304px;
    border-radius: 50%;
    background: var(--olive);
    top: 2px;
  }
  .card--front .emblem-circle { left: 354px; }
  .card--back .emblem-circle { left: -103px; }

  .holder-name {
    position: absolute;
    left: 27px;
    top: 32px;
    margin: 0;
    font-family: "Questrial", sans-serif;
    font-weight: 400;
    font-size: 33px;
    color: var(--ink);
    letter-spacing: 0.2px;
  }
  .holder-title {
    position: absolute;
    left: 28px;
    top: 71px;
    margin: 0;
    font-family: "Fira Sans", sans-serif;
    font-size: 14px;
    color: var(--muted);
  }
  .divider {
    position: absolute;
    left: 28px;
    top: 106px;
    width: 270px;
    height: 1px;
    background: linear-gradient(to right, var(--rule), var(--rule) 80%, rgba(230,230,226,0));
  }
  .company {
    position: absolute;
    left: 27px;
    top: 124px;
    margin: 0;
    font-family: "Fira Sans", sans-serif;
    font-weight: 400;
    font-size: 19px;
    color: var(--ink);
  }
  .address {
    position: absolute;
    left: 29px;
    top: 155px;
    margin: 0;
    font-family: "Fira Sans", sans-serif;
    font-style: normal;
    font-size: 14px;
    line-height: 23px;
    color: var(--muted);
  }
  .contact-list {
    position: absolute;
    left: 26px;
    top: 215px;
    margin: 0;
    padding: 0;
    list-style: none;
    font-family: "Fira Sans", sans-serif;
    font-size: 14px;
    line-height: 19.5px;
    color: var(--muted);
  }
  .contact-list li {
    display: flex;
    align-items: center;
    gap: 9px;
  }
  .contact-icon {
    width: 13px;
    height: 13px;
    flex: none;
  }

  .brand {
    position: absolute;
    left: 246px;
    top: 119px;
    display: flex;
    align-items: center;
    gap: 14px;
  }
  .brand-dot {
    width: 46px;
    height: 46px;
    border-radius: 50%;
    background: var(--olive);
    flex: none;
  }
  .brand-name {
    margin: 0;
    font-family: "Fira Sans", sans-serif;
    font-weight: 600;
    font-size: 30px;
    line-height: 32px;
    color: var(--olive);
  }
</style>
</head>
<body>
<main class="stage">

  <section class="card card--front" aria-label="Card front">
    <div class="emblem-circle" aria-hidden="true"></div>

    <h1 class="holder-name">Dana Reyes</h1>
    <p class="holder-title">Chief Performance Strategist</p>
    <div class="divider"></div>
    <h2 class="company">Brightmoor Lane, Inc.</h2>
    <address class="address">2118 Orchard Ridge Road<br>#410, Fenwick, MI 48210</address>

    <ul class="contact-list">
      <li>
        <svg class="contact-icon" viewBox="0 0 14 14" aria-hidden="true">
          <g fill="none" stroke="#55554d" stroke-width="1">
            <circle cx="7" cy="7" r="6"/>
            <ellipse cx="7" cy="7" rx="2.6" ry="6"/>
            <line x1="1" y1="7" x2="13" y2="7"/>
            <line x1="2" y1="4" x2="12" y2="4"/>
            <line x1="2" y1="10" x2="12" y2="10"/>
          </g>
        </svg>
        www.brightmoorlane.com
      </li>
      <li>
        <svg class="contact-icon" viewBox="0 0 14 14" aria-hidden="true">
          <rect x="1" y="3" width="12" height="8.5" fill="#55554d"/>
          <polyline points="1,3 7,8 13,3" fill="none" stroke="#fff" stroke-width="1"/>
        </svg>
        danar@brightmoorlane.com
      </li>
      <li>
        <svg class="contact-icon" viewBox="0 0 14 14" aria-hidden="true">
          <path d="M1 5 Q7 1 13 5 L12 6.5 L9.5 5.5 L9.5 4.5 Q7 3.8 4.5 4.5 L4.5 5.5 L2 6.5 Z" fill="#55554d"/>
          <path d="M3.5 7 L10.5 7 L12 12 L2 12 Z" fill="#55554d"/>
          <circle cx="7" cy="9.5" r="1.3" fill="#fff"/>
        </svg>
        555 - 201 - 4478
      </li>
      <li>
        <svg class="contact-icon" viewBox="0 0 14 14" aria-hidden="true">
          <rect x="3.5" y="0.5" width="7" height="13" rx="1" fill="#55554d"/>
          <rect x="4.8" y="2" width="4.4" height="7" fill="#fff"/>
          <circle cx="7" cy="11.3" r="0.9" fill="#fff"/>
        </svg>
        555 - 319 - 6602
      </li>
    </ul>
  </section>

  <section class="card card--back" aria-label="Card back">
    <div class="emblem-circle" aria-hidden="true"></div>

    <div class="brand">
      <span class="brand-dot" aria-hidden="true"></span>
      <p class="brand-name">Brightmoor<br>Lane</p>
    </div>
  </section>

</main>
</body>
</html>
```